Full stationary package for technology company installing structured cabling and systems integration
Copper Ridge Networks, LLC.
Full stationary package for technology company installing structured cabling and systems integration - Information Technology
Creative Brief
Simple
Dalton Pruitt
President
7126 Fennick Ln. Sylvania, OH 43817
dalton@copperridgenet.example
copperridgenet.example
Contact info to be added on one side and only the logo on the other side
Copperridge Copperridge
Going through all of the current files, please do not unload anymore concepts, I like we have enough to select from before edits. Thank you for all of the submissions.
Copper Ridge Networks Logo Information Fonts Used: * BankGothic Md BT Medium Colours used (CMYK): Light Green: 50 0 99 0 Dark Green: 87 23 86 25 Black 0 0 0 100

```html
<!DOCTYPE html>
<html lang="en">
<head>
<meta charset="utf-8">
<title>Copper Ridge Networks — Stationery Concepts</title>
<link href="https://fonts.googleapis.com/css2?family=Michroma&family=Roboto:wght@400;700&family=Pinyon+Script&display=swap" rel="stylesheet">
<style>
:root{
  --bg:#9b9b9b;
  --paper:#ffffff;
  --ink:#222222;
  --muted:#8a8a8a;
  --green-dark:#16602e;
  --green:#25913c;
  --green-light:#8cc63f;
  --charcoal:#262626;
  --rule:#d6d6d6;
}
*{margin:0;padding:0;box-sizing:border-box}
html,body{width:1200px;height:254px;overflow:hidden;background:var(--bg);font-family:"Roboto",Arial,sans-serif;color:var(--ink)}
.canvas{position:relative;width:1200px;height:254px}
.piece{position:absolute;background:var(--paper);overflow:hidden;box-shadow:0 1px 2px rgba(0,0,0,.35)}
.piece.dark{background:var(--charcoal);color:#fff}
.band{position:absolute;left:0;right:0;background:linear-gradient(90deg,var(--green-dark),var(--green),var(--green-light))}
.micro{font-size:1.8px;line-height:2.4px;color:var(--muted)}

/* brand name lockup */
.mark{display:flex;align-items:center;gap:1.5px;white-space:nowrap}
.mark .dot{width:4px;height:4px;border-radius:50%;background:var(--green);flex:none}
.mark .name{font-family:"Michroma",Arial,sans-serif;color:var(--ink);font-size:3.2px;letter-spacing:.15px}
.dark .mark .name{color:#fff}
.mark.lg .dot{width:8px;height:8px}
.mark.lg .name{font-size:6px}

/* intro */
.intro{position:absolute;left:34px;top:26px;width:44px;text-align:center}
.intro .mark{justify-content:center}
.intro p{font-size:3.6px;color:#333;margin-top:2px;white-space:nowrap;margin-left:-6px;margin-right:-6px}

/* business card */
.card{width:48px;height:26px}
.card .band{top:0;height:3px}
.card .tag{position:absolute;top:.7px;left:0;right:0;text-align:center;font-size:1.5px;color:#fff;letter-spacing:.2px}
.card .mark{position:absolute;left:3px;top:12px}
.card .who{position:absolute;left:26px;top:5px;width:21px}
.card .who b{display:block;font-size:2.2px;color:var(--green-dark)}
.card.back .mark{left:50%;top:50%;transform:translate(-50%,-50%)}
.card.back.banded .mark{top:57%}

/* letterhead & fax */
.sheet{width:78px;height:100px}
.sheet .mark{position:absolute;left:5px;top:6px}
.sheet .addr{position:absolute;right:4px;top:5px;width:24px}
.sheet .body{position:absolute;left:5px;right:5px;top:22px}
.sheet .body p{margin-bottom:2px}
.sheet .sign{font-family:"Pinyon Script",cursive;font-size:5px;line-height:6px;color:var(--ink)}
.sheet .foot{position:absolute;left:0;right:0;bottom:3px;text-align:center}
.sheet .band{bottom:0;height:1.5px}
.fax-grid{position:absolute;left:4px;right:4px;top:20px;display:grid;grid-template-columns:1fr 2fr 1fr 2fr;gap:.8px}
.fax-grid span{font-size:1.8px;height:3.4px;line-height:3.4px;background:#ececec;padding-left:1px;color:#666}
.fax-checks{position:absolute;left:4px;right:4px;top:38px;display:flex;justify-content:space-between}
.fax-checks span{font-size:1.6px;color:#666;display:flex;align-items:center;gap:.6px}
.fax-checks i{width:1.8px;height:1.8px;border:.3px solid #666;display:inline-block}
.fax-comment{position:absolute;left:4px;top:43px;font-size:2px;color:#444}

/* email signature */
.esig{width:55px;height:28px}
.esig .band{top:0;height:3px}
.esig .tag{position:absolute;top:.7px;left:0;right:0;text-align:center;font-size:1.5px;color:#fff}
.esig .mark{position:absolute;left:3px;top:13px}
.esig .who{position:absolute;left:28px;top:6px;width:25px}
.esig .who b{display:block;font-size:2.2px;color:var(--green-dark)}
.esig .band.b{top:auto;bottom:0;height:1.5px}

/* envelopes */
.env{width:84px;height:37px}
.env .band{bottom:0;height:3px}
.env .mark{position:absolute;left:3px;top:4px}
.env .addr{position:absolute;left:3px;top:10px;width:30px}
.env .flap{position:absolute;left:0;right:0;top:0;height:14px;background:linear-gradient(180deg,var(--green-dark),var(--green));clip-path:polygon(0 0,100% 0,92% 100%,8% 100%)}
.env .url{position:absolute;left:0;right:0;top:6px;text-align:center;font-size:1.8px;color:#fff}
.env.back .mark{left:50%;top:20px;transform:translateX(-50%)}
.env.back .flap.charcoal{background:var(--charcoal)}

/* folder */
.folder{width:125px;height:98px;background:transparent;box-shadow:none}
.folder .outer{position:absolute;left:0;top:0;width:62px;height:98px;background:var(--charcoal);border-left:2px solid var(--green)}
.folder .outer .addr{position:absolute;left:4px;bottom:8px;color:#bbb}
.folder .front{position:absolute;left:62px;top:2px;width:63px;height:94px;background:#fff;border-right:2px solid var(--green)}
.folder .front .mark{position:absolute;left:50%;top:40px;transform:translateX(-50%)}
.folder .front .mark .name{font-size:4px}
.insert{width:125px;height:76px}
.insert .side{position:absolute;top:0;bottom:0;width:3px;background:var(--green)}
.insert .pocket{position:absolute;left:10px;right:10px;bottom:0;height:28px;background:var(--charcoal);clip-path:polygon(0 15%,40% 0,50% 100%,60% 0,100% 15%,100% 100%,0 100%)}

/* compliment & thank you */
.slip{width:86px;height:37px}
.slip .band{top:0;height:2.5px}
.slip .band.b{top:auto;bottom:0}
.slip .mark{position:absolute;left:4px;top:9px}
.slip .addr{position:absolute;right:4px;top:6px;width:24px}
.slip .script{position:absolute;left:24px;top:20px;font-family:"Pinyon Script",cursive;font-size:7px;color:#333;white-space:nowrap}
.ty{width:50px;height:37px}
.ty .band{top:0;height:2px}
.ty .mark{position:absolute;left:50%;top:7px;transform:translateX(-50%)}
.ty .script{position:absolute;left:0;right:0;top:17px;text-align:center;font-family:"Pinyon Script",cursive;font-size:9px;color:#333;white-space:nowrap}
.ty.dark .addr{position:absolute;left:3px;right:3px;bottom:7px;text-align:center;color:#bbb}

/* discs & covers */
.disc{position:absolute;width:58px;height:58px;border-radius:50%;box-shadow:0 1px 2px rgba(0,0,0,.4);overflow:hidden}
.disc .hole{position:absolute;left:50%;top:50%;width:13px;height:13px;margin:-6.5px 0 0 -6.5px;border-radius:50%;background:#fff;border:2.5px solid #333}
.disc .mark{position:absolute;left:50%;top:10px;transform:translateX(-50%)}
.disc .url{position:absolute;left:0;right:0;bottom:9px;text-align:center;font-size:1.8px}
.disc.green{background:radial-gradient(circle,var(--green-light),var(--green) 55%,var(--green-dark))}
.disc.green .name,.disc.green .url{color:#fff}
.disc.green .dot{background:#fff}
.disc.black{background:var(--charcoal);border:1.5px solid var(--green)}
.disc.black.white-rim{border-color:#fff}
.disc.black .name,.disc.black .url{color:#fff}
.disc.white{background:#fff;border:1.5px solid #333}
.coaster{position:absolute;width:21px;height:21px;border-radius:50%;border:1px solid #fff;display:flex;align-items:center;justify-content:center;box-shadow:0 1px 2px rgba(0,0,0,.4)}
.coaster .dot{width:5px;height:5px;border-radius:50%;background:var(--green)}
.coaster.light{background:#fff;border-color:var(--green)}
.coaster.green{background:var(--green)}
.coaster.green .dot{background:#fff}
.coaster.black{background:var(--charcoal)}
.cover{width:66px;height:50px}
.cover .mark{position:absolute;left:4px;top:7px}
.cover .addr{position:absolute;left:4px;right:4px;bottom:5px}
.cover .band{bottom:0;height:1.5px}
.case{width:58px;height:41px}
.case .mark{position:absolute;left:4px;top:8px}
.case .addr{position:absolute;left:4px;right:4px;bottom:4px}

/* presentation slides, authored at 2x and scaled to fit */
.slide{width:186px;height:140px;transform:scale(.5);transform-origin:0 0}
.slide .band{top:0;height:4px}
.slide .band.b{top:auto;bottom:0;height:3px}
.slide h3{position:absolute;left:12px;top:12px;font-size:9px;font-weight:400;color:#333}
.slide h4{position:absolute;left:12px;top:23px;font-size:5px;font-weight:700;color:var(--green)}
.slide .corner{position:absolute;right:12px;top:14px;width:6px;height:6px;border-radius:50%;background:var(--green)}
.slide .rule{position:absolute;left:12px;right:12px;top:31px;height:.6px;background:var(--rule)}
.slide .foot{position:absolute;left:0;right:0;bottom:8px;text-align:center}
.slide .micro{font-size:3px;line-height:3.8px}
.title-slide .mark{position:absolute;left:50%;top:36px;transform:translateX(-50%)}
.title-slide .mark .dot{width:14px;height:14px}
.title-slide .mark .name{font-size:10px}
.title-slide .lines{position:absolute;left:0;right:0;top:66px;text-align:center;color:var(--green-dark)}
.title-slide .lines .a{font-size:9px}
.title-slide .lines .b{font-size:11px;font-weight:700;color:#222}
.title-slide .lines .c{font-size:9px}
.team{position:absolute;left:12px;right:12px;top:40px;display:grid;grid-template-columns:repeat(4,1fr);gap:6px}
.team .photo{height:34px;background:#5a5a5a;color:#ddd;font-size:4px;display:flex;align-items:center;justify-content:center}
.team b{display:block;font-size:3.6px;margin-top:5px}
.team em{display:block;font-style:normal;font-size:3.2px;color:var(--green)}
.groups{position:absolute;left:12px;right:12px;top:38px;display:grid;grid-template-columns:1fr 1fr;gap:6px 14px}
.groups b{display:block;font-size:4px;margin-bottom:1px;color:var(--green-dark)}
.chart{position:absolute;left:14px;top:40px}
.aside{position:absolute;left:104px;right:12px;top:42px}
.below{position:absolute;left:12px;right:12px;top:112px}
.pie-text{position:absolute;left:12px;top:40px;width:98px}
.pie{position:absolute;left:124px;top:44px}
.pie-legend{position:absolute;left:124px;top:96px;width:54px}
.thanks{position:absolute;right:24px;top:40px;text-align:center;color:#fff}
.thanks .t1{font-size:28px;line-height:32px;letter-spacing:.5px}
.thanks .t2{font-size:15px;line-height:18px}
.slide.dark .foot{color:#aaa}
</style>
</head>
<body>
<main class="canvas">

  <section class="intro">
    <div class="mark lg"><span class="dot"></span><span class="name">COPPER RIDGE</span></div>
    <p>Stationery Concepts</p>
  </section>

  <!-- business cards -->
  <article class="piece card" style="left:6px;top:57px">
    <div class="band"></div><div class="tag">CABLING &amp; SYSTEMS INTEGRATION</div>
    <div class="mark"><span class="dot"></span><span class="name">COPPER RIDGE</span></div>
    <div class="who micro"><b>DALTON PRUITT</b>President<br>7126 Fennick Ln.<br>Harlow Springs, MN 55820<br>(612) 555-0142<br>dalton@copperridgenet.example</div>
  </article>
  <article class="piece card" style="left:58px;top:57px">
    <div class="band"></div><div class="tag">CABLING &amp; SYSTEMS INTEGRATION</div>
    <div class="mark"><span class="dot"></span><span class="name">COPPER RIDGE</span></div>
    <div class="who micro"><b>DALTON PRUITT</b>President<br>7126 Fennick Ln.<br>Harlow Springs, MN 55820<br>(612) 555-0142<br>copperridgenet.example</div>
  </article>
  <article class="piece card back" style="left:6px;top:90px">
    <div class="mark"><span class="dot"></span><span class="name">COPPER RIDGE</span></div>
  </article>
  <article class="piece card back banded" style="left:58px;top:90px">
    <div class="band"></div><div class="tag">CABLING &amp; SYSTEMS INTEGRATION</div>
    <div class="mark"><span class="dot"></span><span class="name">COPPER RIDGE</span></div>
  </article>

  <!-- letterheads -->
  <article class="piece sheet" style="left:109px;top:16px">
    <div class="mark"><span class="dot"></span><span class="name">COPPER RIDGE</span></div>
    <div class="addr micro">7126 Fennick Ln.<br>Harlow Springs, MN 55820<br>(612) 555-0142<br>dalton@copperridgenet.example</div>
    <div class="body micro">
      <p>Date</p>
      <p>Recipient Name<br>Company Name<br>Street Address<br>City, State, Zip</p>
      <p>Thank you for your time today. We install structured cabling and integrate systems for offices of every size, from a single floor to a full campus.</p>
      <p>Our team plans each run, labels every port and tests every link before handover, so your network is ready on day one.</p>
      <p>Please reach out with any questions about the proposal.</p>
      <p>Sincerely,</p>
      <div class="sign">Dalton Pruitt</div>
      <p>Dalton Pruitt, President</p>
    </div>
    <div class="foot micro">copperridgenet.example</div>
    <div class="band"></div>
  </article>
  <article class="piece sheet" style="left:192px;top:16px">
    <div class="mark" style="left:50%;transform:translateX(-50%)"><span class="dot"></span><span class="name">COPPER RIDGE</span></div>
    <div class="body micro">
      <p>Date</p>
      <p>Recipient Name<br>Company Name<br>Street Address<br>City, State, Zip</p>
      <p>Thank you for your time today. We install structured cabling and integrate systems for offices of every size, from a single floor to a full campus.</p>
      <p>Our team plans each run, labels every port and tests every link before handover.</p>
      <p>Sincerely,</p>
      <div class="sign">Dalton Pruitt</div>
      <p>Dalton Pruitt, President</p>
    </div>
    <div class="foot micro">7126 Fennick Ln. Harlow Springs, MN 55820 · copperridgenet.example</div>
    <div class="band"></div>
  </article>

  <!-- email signature -->
  <article class="piece esig" style="left:293px;top:42px">
    <div class="band"></div><div class="tag">CABLING &amp; SYSTEMS INTEGRATION</div>
    <div class="mark"><span class="dot"></span><span class="name">COPPER RIDGE</span></div>
    <div class="who micro"><b>DALTON PRUITT</b>President<br>7126 Fennick Ln.<br>Harlow Springs, MN 55820<br>(612) 555-0142</div>
    <div class="band b"></div>
  </article>

  <!-- envelopes -->
  <article class="piece env" style="left:275px;top:80px">
    <div class="mark"><span class="dot"></span><span class="name">COPPER RIDGE</span></div>
    <div class="addr micro">7126 Fennick Ln.<br>Harlow Springs, MN 55820</div>
    <div class="band"></div>
  </article>
  <article class="piece env back" style="left:375px;top:40px">
    <div class="flap"></div><div class="url">copperridgenet.example</div>
    <div class="mark"><span class="dot"></span><span class="name">COPPER RIDGE</span></div>
  </article>
  <article class="piece env back" style="left:364px;top:80px">
    <div class="flap charcoal"></div><div class="url">copperridgenet.example</div>
    <div class="mark"><span class="dot"></span><span class="name">COPPER RIDGE</span></div>
  </article>

  <!-- folder -->
  <article class="piece folder" style="left:465px;top:19px">
    <div class="outer"><div class="addr micro">7126 Fennick Ln.<br>Harlow Springs, MN 55820<br>(612) 555-0142<br>copperridgenet.example</div></div>
    <div class="front"><div class="mark"><span class="dot"></span><span class="name">COPPER RIDGE</span></div></div>
  </article>
  <article class="piece insert" style="left:474px;top:137px">
    <div class="side" style="left:0"></div><div class="side" style="right:0"></div>
    <div class="pocket"></div>
  </article>

  <!-- fax sheets -->
  <article class="piece sheet" style="left:594px;top:16px">
    <div class="mark"><span class="dot"></span><span class="name">COPPER RIDGE</span></div>
    <div class="addr micro">7126 Fennick Ln.<br>Harlow Springs, MN 55820<br>(612) 555-0142</div>
    <div class="fax-grid"><span>To</span><span></span><span>From</span><span></span><span>Fax</span><span></span><span>Pages</span><span></span><span>Phone</span><span></span><span>Date</span><span></span><span>Re</span><span></span><span>CC</span><span></span></div>
    <div class="fax-checks"><span><i></i>Urgent</span><span><i></i>Review</span><span><i></i>Comment</span><span><i></i>Reply</span></div>
    <div class="fax-comment">Comments :</div>
    <div class="foot micro">copperridgenet.example</div>
    <div class="band"></div>
  </article>
  <article class="piece sheet" style="left:677px;top:16px">
    <div class="mark" style="left:50%;transform:translateX(-50%)"><span class="dot"></span><span class="name">COPPER RIDGE</span></div>
    <div class="fax-grid"><span>To</span><span></span><span>From</span><span></span><span>Fax</span><span></span><span>Pages</span><span></span><span>Phone</span><span></span><span>Date</span><span></span><span>Re</span><span></span><span>CC</span><span></span></div>
    <div class="fax-checks"><span><i></i>Urgent</span><span><i></i>Review</span><span><i></i>Comment</span><span><i></i>Reply</span></div>
    <div class="fax-comment">Comments :</div>
    <div class="foot micro">7126 Fennick Ln. Harlow Springs, MN 55820</div>
    <div class="band"></div>
  </article>

  <!-- compliment slip & thank you -->
  <article class="piece slip" style="left:770px;top:27px">
    <div class="band"></div>
    <div class="mark"><span class="dot"></span><span class="name">COPPER RIDGE</span></div>
    <div class="addr micro">7126 Fennick Ln.<br>Harlow Springs, MN 55820<br>(612) 555-0142<br>copperridgenet.example</div>
    <div class="script">With Compliments</div>
    <div class="band b"></div>
  </article>
  <article class="piece ty" style="left:763px;top:73px">
    <div class="band"></div>
    <div class="mark"><span class="dot"></span><span class="name">COPPER RIDGE</span></div>
    <div class="script">Thank you</div>
  </article>
  <article class="piece ty dark" style="left:818px;top:73px">
    <div class="addr micro">7126 Fennick Ln. Harlow Springs, MN 55820<br>dalton@copperridgenet.example</div>
  </article>

  <!-- top disc & case -->
  <div class="disc black" style="left:870px;top:7px;border-color:var(--charcoal)"><div class="mark"><span class="dot"></span><span class="name">COPPER RIDGE</span></div><div class="hole"></div><div class="url">copperridgenet.example</div></div>
  <article class="piece cover" style="left:934px;top:11px">
    <div class="mark"><span class="dot"></span><span class="name">COPPER RIDGE</span></div>
    <div class="addr micro">7126 Fennick Ln. Harlow Springs, MN 55820 · copperridgenet.example</div>
    <div class="band"></div>
  </article>

  <!-- bottom discs -->
  <div class="disc green" style="left:682px;top:127px"><div class="mark"><span class="dot"></span><span class="name">COPPER RIDGE</span></div><div class="hole"></div><div class="url">copperridgenet.example</div></div>
  <div class="disc black" style="left:747px;top:127px"><div class="mark"><span class="dot"></span><span class="name">COPPER RIDGE</span></div><div class="hole"></div><div class="url">copperridgenet.example</div></div>
  <div class="disc white" style="left:683px;top:191px"><div class="mark"><span class="dot"></span><span class="name">COPPER RIDGE</span></div><div class="hole"></div><div class="url">copperridgenet.example</div></div>
  <div class="disc black white-rim" style="left:749px;top:191px"><div class="mark"><span class="dot"></span><span class="name">COPPER RIDGE</span></div><div class="hole"></div><div class="url">copperridgenet.example</div></div>

  <!-- coasters -->
  <div class="coaster light" style="left:485px;top:222px"><span class="dot"></span></div>
  <div class="coaster green" style="left:511px;top:222px"><span class="dot"></span></div>
  <div class="coaster black" style="left:537px;top:222px"><span class="dot"></span></div>
  <div class="coaster light" style="left:563px;top:222px"><span class="dot"></span></div>

  <!-- disc sleeves -->
  <article class="piece case dark" style="left:820px;top:142px">
    <div class="mark"><span class="dot"></span><span class="name">COPPER RIDGE</span></div>
    <div class="addr micro" style="color:#bbb">7126 Fennick Ln. Harlow Springs, MN 55820<br>copperridgenet.example</div>
  </article>
  <article class="piece case" style="left:820px;top:196px">
    <div class="mark"><span class="dot"></span><span class="name">COPPER RIDGE</span></div>
    <div class="addr micro">7126 Fennick Ln. Harlow Springs, MN 55820<br>copperridgenet.example</div>
  </article>

  <!-- presentation: title -->
  <article class="piece slide title-slide" style="left:1001px;top:13px">
    <div class="band"></div>
    <div class="mark"><span class="dot"></span><span class="name">COPPER RIDGE</span></div>
    <div class="lines"><div class="a">Welcome to Our</div><div class="b">Presentation Name</div><div class="c">Description</div></div>
    <div class="band b"></div>
  </article>

  <!-- presentation: team -->
  <article class="piece slide" style="left:1101px;top:13px">
    <div class="band"></div>
    <h3>Heading Here</h3><h4>Sub Heading</h4><span class="corner"></span><div class="rule"></div>
    <div class="team">
      <div><div class="photo" role="img" aria-label="Team member photo">Photo</div><b>Team member1</b><em>Title</em><div class="micro">Short bio line for this person.</div></div>
      <div><div class="photo" role="img" aria-label="Team member photo">Photo</div><b>Team member2</b><em>Title</em><div class="micro">Short bio line for this person.</div></div>
      <div><div class="photo" role="img" aria-label="Team member photo">Photo</div><b>Team member3</b><em>Title</em><div class="micro">Short bio line for this person.</div></div>
      <div><div class="photo" role="img" aria-label="Team member photo">Photo</div><b>Team member4</b><em>Title</em><div class="micro">Short bio line for this person.</div></div>
    </div>
    <div class="band b"></div>
  </article>

  <!-- presentation: groups -->
  <article class="piece slide" style="left:1001px;top:89px">
    <div class="band"></div>
    <h3>Heading Here</h3><h4>Sub Heading</h4><span class="corner"></span><div class="rule"></div>
    <div class="groups">
      <div><b>Group1</b><div class="micro">Cabling plans drawn per floor with labeled runs and rack layouts for each closet.</div></div>
      <div><b>Group4</b><div class="micro">Fiber backbone installed and certified between every closet on site.</div></div>
      <div><b>Group2</b><div class="micro">Wireless survey done before any access points are mounted.</div></div>
      <div><b>Group5</b><div class="micro">Security cameras and door access joined on one network.</div></div>
      <div><b>Group3</b><div class="micro">Every link tested and recorded in the handover report.</div></div>
      <div><b>Group6</b><div class="micro">Ongoing support with clear response times for clients.</div></div>
    </div>
    <div class="band b"></div>
  </article>

  <!-- presentation: bar chart -->
  <article class="piece slide" style="left:1101px;top:89px">
    <div class="band"></div>
    <h3>Heading Here</h3><h4>Sub Heading</h4><span class="corner"></span><div class="rule"></div>
    <svg class="chart" width="82" height="64" viewBox="0 0 82 64">
      <g stroke="#e2e2e2" stroke-width=".5"><line x1="0" y1="12" x2="82" y2="12"/><line x1="0" y1="26" x2="82" y2="26"/><line x1="0" y1="40" x2="82" y2="40"/><line x1="0" y1="54" x2="82" y2="54"/></g>
      <g fill="#222"><rect x="4" y="36" width="10" height="28"/><rect x="20" y="30" width="10" height="34"/><rect x="36" y="20" width="10" height="44"/><rect x="52" y="12" width="10" height="52"/><rect x="68" y="4" width="10" height="60"/></g>
    </svg>
    <div class="aside micro">Installed links grew each year as new offices joined. The chart shows certified drops per year across all sites, with fiber runs counted once per closet.</div>
    <div class="below micro">Figures are taken from handover reports and include only links that passed full testing.</div>
    <div class="band b"></div>
  </article>

  <!-- presentation: pie chart -->
  <article class="piece slide" style="left:1001px;top:165px">
    <div class="band"></div>
    <h3>Heading Here</h3><h4>Sub Heading</h4><span class="corner"></span><div class="rule"></div>
    <div class="pie-text micro">Work by type over the past year. Copper cabling remains the largest share, with fiber and wireless projects growing steadily alongside camera and access systems for our clients across the region.</div>
    <svg class="pie" width="46" height="46" viewBox="-23 -23 46 46">
      <circle r="21" fill="#222"/>
      <path d="M0 0 L0 -21 A21 21 0 0 1 20 6.3 Z" fill="var(--green-dark)"/>
      <path d="M0 0 L20 6.3 A21 21 0 0 1 4.2 20.6 Z" fill="var(--green)"/>
      <path d="M0 0 L4.2 20.6 A21 21 0 0 1 -10.5 18.2 Z" fill="var(--green-light)"/>
    </svg>
    <div class="pie-legend micro">Copper 48% · Fiber 22%<br>Wireless 15% · Systems 15%</div>
    <div class="band b"></div>
  </article>

  <!-- presentation: thanks -->
  <article class="piece slide dark" style="left:1101px;top:165px">
    <div class="thanks"><div class="t1">Thanks</div><div class="t2">For Coming</div></div>
    <div class="foot micro">7126 Fennick Ln. Harlow Springs, MN 55820 · dalton@copperridgenet.example · copperridgenet.example</div>
  </article>

</main>
</body>
</html>
```